Business Card for a Floral & Decorating Business

I would like to take my current logo and create a better business card. I am looking for elegance as I am a florist and event decorator. My logo has multiple colour options. I like colours like green, purple, pink and orange, I think I would like a white card, open to black back ground. I want it to feel elegant and romantic. I like metallic lettering that maybe is indented in the paper, I also like glossy paper. I have a full logo already as well as a badge. I have attached both in multiple colours.m
Updates

Need extra days to review

Target Market(s)

Weddings, special events, floral customers

Industry/Entity Type

Floral and decorating

Contact Information for Business Card

Phone number, email, instagram, facebook, title, name, logo

Font styles to use
Script

Requirements
Nice to have
• Elegant

```html
<!DOCTYPE html>
<html lang="en">
<head>
<meta charset="utf-8">
<title>Larkmoor Hollis – Business Card</title>
<link rel="stylesheet" href="https://fonts.googleapis.com/css2?family=Raleway:wght@300;400;500;600&display=swap">
<style>
  :root {
    --backdrop: #2b2b2b;
    --card-white: #ffffff;
    --card-black: #141414;
    --brand-green: #4f8a7b;
    --accent-rose: #a3385e;
    --text-grey: #5a5a5a;
    --sheen: rgba(255, 255, 255, 0.07);
  }
  * { box-sizing: border-box; margin: 0; padding: 0; }
  html, body {
    width: 1200px; height: 800px; overflow: hidden;
    background: var(--backdrop);
    font-family: "Raleway", sans-serif;
  }
  .canvas { position: relative; width: 1200px; height: 800px; }
  .card {
    position: absolute; left: 390px; width: 420px; height: 240px; overflow: hidden;
  }
  .card-front { top: 130px; background: var(--card-white); }
  .card-back {
    top: 430px;
    background:
      radial-gradient(ellipse 60% 90% at 92% 40%, var(--sheen) 0%, transparent 70%),
      linear-gradient(100deg, #0f0f0f 0%, #161616 55%, #262626 100%);
  }

  /* Front: brand block */
  .brand {
    position: absolute; left: 14px; top: 84px; width: 200px;
    text-align: center; color: var(--brand-green);
  }
  .brand-mark {
    display: block; margin: 0 auto 10px;
    width: 22px; height: 22px; border-radius: 50%;
    border: 1.2px solid var(--brand-green);
  }
  .brand-name {
    font-size: 17px; font-weight: 300; letter-spacing: 3px;
    text-transform: lowercase; white-space: nowrap; line-height: 1;
  }
  .brand-tagline {
    margin-top: 8px; font-size: 5.5px; font-weight: 500;
    letter-spacing: 2px; text-transform: uppercase;
  }
  .divider {
    position: absolute; left: 209px; top: 81px;
    width: 1.5px; height: 79px; background: var(--accent-rose);
  }

  /* Front: contact block */
  .contact { position: absolute; left: 227px; top: 78px; color: var(--text-grey); }
  .contact-name {
    font-size: 16px; font-weight: 600; color: var(--brand-green); line-height: 1.2;
  }
  .contact-title { font-size: 11.5px; font-weight: 400; line-height: 1.3; }
  .contact-details { margin-top: 10px; font-size: 11.2px; font-weight: 400; line-height: 1.3; }

  /* Back: glossy black with one rose accent */
  .back-accent {
    position: absolute; right: 46px; top: 137px;
    display: flex; align-items: center; gap: 8px;
    color: var(--accent-rose);
  }
  .back-accent-name {
    font-size: 11px; font-weight: 300; letter-spacing: 2px;
    text-transform: lowercase; white-space: nowrap;
  }
  .back-accent-mark {
    width: 24px; height: 24px; border-radius: 50%; background: var(--accent-rose);
  }
</style>
</head>
<body>
<main class="canvas">
  <section class="card card-front" aria-label="Business card front">
    <div class="brand">
      <span class="brand-mark"></span>
      <div class="brand-name">Larkmoor Hollis</div>
      <div class="brand-tagline">Decorating &amp; Florals.</div>
    </div>
    <div class="divider"></div>
    <div class="contact">
      <div class="contact-name">DANA WHITFIELD</div>
      <div class="contact-title">President &amp; CEO</div>
      <div class="contact-details">
        <div>000-000-0000</div>
        <div>d.whitfield@larkmoor-demo.com</div>
        <div>www.larkmoor-demo.com</div>
      </div>
    </div>
  </section>

  <section class="card card-back" role="img"
    aria-label="Glossy black card back with a repeating embossed floral monogram pattern and one rose-coloured accent">
    <div class="back-accent">
      <span class="back-accent-name">Larkmoor Hollis</span>
      <span class="back-accent-mark"></span>
    </div>
  </section>
</main>
</body>
</html>
```